Unique Playing Card Deck Design

Brief:

I am looking for a designer to design a whole deck of cards from the ground up. I would like both the front and back designed for the deck, and would like the desk to include all the standard cards including jokers. I would like to make each card as unique as possible, so including original designs and artwork for the non-face cards as well.

I would like these cards to be poker size (63mm x 88mm, 2.5" x 3.5") or B8 size according to ISO 216) and I’ve attached a template that should be followed for the sizing.

No real limit on the design so be as creative as you can!

Design Details

Color Mode: RGB or CYMK for color images, Grayscale for black and white

File types: JPG, BMP, PNG, GIF, TIFF

Image resolution: Minimum 300 dpi

Bleeding: Allow 1/8" (approx 36 pixels based on a 300dpi image) for bleeding and a further 1/8" for safe area margin inside each side

EDIT: Because this project requires a lot of design work I am fine for the submissions to be limited to 3 or 4 cards that would demonstrate the overall direction that you are taking. Once I have chosen the designs we can continue refining them and adding the rest of the deck. I would also like a box for the cards to be designed and can provide a template after I have chosen the designers. Thanks and please let me know if you have any questions!

EDIT2: I realize this project is a lot of work and so I have taken the amounts that I had for 2nd and 3rd place and increased the reward for 1st place. I am still interested in selecting multiple designs, but because this project is being done on a committed payment basis I wanted to ensure that I was only obligated to select one design. However, if there are multiple designs that I am interested in, I will award the design work to an additional 1-3 designers (to a maximum of 4 total) on the same terms as 1st place. i.e. all designers selected will be paid the same amount. Thanks again for looking!

Target Market(s)

Adult card players who appreciate good design (i.e. the designs should not be cartoon-like or targeted at children). These are going to be premium cards printed on the best quality paper etc so I would like the design to reflect this.

Font styles to use
Decorative
Script

Requirements
Nice to have
• I will leave the design idea up to you but I like the look of really old playing cards (think of a deck of medieval playing cards for example). I also like the art deco kind of aesthetic. On the complete opposite side of the spectrum a very modern looking, minimalist design is also appealing.
• These are just a few ideas but as I said I am really open to anything. It just needs to be a bold, original design.

```html
<!DOCTYPE html>
<html lang="en">
<head>
<meta charset="utf-8">
<title>Playing Card Deck</title>
<link rel="stylesheet" href="https://fonts.googleapis.com/css2?family=Dancing+Script:wght@400;600&display=swap">
<style>
  :root {
    --page: #ffffff;
    --edge: #e4e4e4;
    --frame: #f1e1ee;
    --frame-line: #e8cfe3;
    --ink: #1c1a1a;
    --red: #b0101a;
    --gold: #c9a54a;
    --pink: #d12f7c;
    --pink-soft: #eab3cc;
    --teal: #1d7a9a;
    --navy: #1f2a44;
    --shadow: rgba(0,0,0,0.18);
  }
  * { margin: 0; padding: 0; box-sizing: border-box; }
  html, body { width: 1200px; height: 900px; overflow: hidden; background: var(--page); }
  body { position: relative; border: 1px solid var(--edge); font-family: "Dancing Script", cursive; }
  .suit-defs { position: absolute; width: 0; height: 0; }
  .deck {
    position: absolute; left: 46px; top: 53px;
    display: grid;
    grid-template-columns: repeat(13, 76px);
    grid-auto-rows: 132px;
    column-gap: 10.3px; row-gap: 28px;
  }
  .card {
    position: relative; width: 76px; height: 132px;
    background: #fff;
    border: 3px solid var(--frame);
    box-shadow: inset 0 0 0 1px var(--frame-line);
    overflow: hidden;
  }
  .rank { position: absolute; left: 4px; top: 1px; font-size: 13px; font-style: italic; color: var(--ink); line-height: 1; }
  .pip { position: absolute; left: 23px; top: 32px; width: 24px; height: 50px; }
  .pip-top { fill: var(--ink); }
  .pip-main { fill: var(--red); stroke: var(--gold); stroke-width: 0.8; }
  .pip-shadow { fill: var(--shadow); }
  .pattern-band {
    position: absolute; left: 4px; right: 4px; bottom: 5px; height: 24px;
    background: linear-gradient(90deg, var(--pink) 0%, var(--pink-soft) 30%, var(--gold) 50%, var(--teal) 75%, var(--pink) 100%);
    opacity: 0.55;
    -webkit-mask-image: linear-gradient(to top, #000 40%, transparent 100%);
            mask-image: linear-gradient(to top, #000 40%, transparent 100%);
  }
  .pattern-band.top {
    top: 5px; bottom: auto;
    -webkit-mask-image: linear-gradient(to bottom, #000 40%, transparent 100%);
            mask-image: linear-gradient(to bottom, #000 40%, transparent 100%);
  }
  .face-art {
    position: absolute; left: 19px; top: 22px; width: 42px; height: 72px;
    background: linear-gradient(160deg, var(--gold) 0%, var(--red) 35%, var(--navy) 70%, var(--ink) 100%);
    border-radius: 12px 12px 2px 2px;
  }
  .corner { position: absolute; width: 11px; height: 11px; fill: var(--ink); }
  .corner.tr { right: 4px; top: 5px; }
  .corner.bl { left: 4px; top: 80px; }
  .ace-pip { position: absolute; left: 14px; top: 20px; width: 46px; height: 80px; }
  .ace-pip .big { fill: var(--ink); stroke: var(--gold); stroke-width: 0.4; }
  .joker-mark { position: absolute; left: 0; right: 0; top: 14px; text-align: center; font-size: 46px; font-weight: 600; color: var(--ink); line-height: 1; }
  .joker-label { position: absolute; left: 0; right: 0; top: 74px; text-align: center; font-size: 15px; font-style: italic; font-weight: 600; color: var(--ink); }
  .back-title { position: absolute; left: 0; right: 0; top: 34px; text-align: center; font-size: 11px; color: var(--ink); }
  .ribbon { position: absolute; left: 6px; top: 48px; width: 64px; height: 20px; }
  .ribbon path { fill: var(--teal); }
</style>
</head>
<body>
<svg class="suit-defs" aria-hidden="true">
  <defs>
    <symbol id="heart" viewBox="0 0 20 20"><path d="M10 18C3 12 1 9 1 6C1 3 3 1 5.5 1C7.5 1 9 2.5 10 4C11 2.5 12.5 1 14.5 1C17 1 19 3 19 6C19 9 17 12 10 18Z"/></symbol>
    <symbol id="diamond" viewBox="0 0 20 20"><path d="M10 0L17 10L10 20L3 10Z"/></symbol>
    <symbol id="spade" viewBox="0 0 20 20"><path d="M10 1C13 6 19 8 19 12C19 15 16 16.5 13 14.5C13.5 17 14.5 18.5 16 19L4 19C5.5 18.5 6.5 17 7 14.5C4 16.5 1 15 1 12C1 8 7 6 10 1Z"/></symbol>
    <symbol id="club" viewBox="0 0 20 20"><circle cx="10" cy="5.5" r="4.5"/><circle cx="5" cy="11.5" r="4.5"/><circle cx="15" cy="11.5" r="4.5"/><path d="M9 10L11 10L12.5 19L7.5 19Z"/></symbol>
    <symbol id="pip-heart" viewBox="0 0 24 50"><use href="#heart" class="pip-top" x="8" y="0" width="8" height="8"/><use href="#heart" class="pip-main" x="2" y="9" width="20" height="20"/><ellipse class="pip-shadow" cx="12" cy="44" rx="8" ry="2"/></symbol>
    <symbol id="pip-diamond" viewBox="0 0 24 50"><use href="#diamond" class="pip-top" x="8" y="0" width="8" height="9"/><use href="#diamond" class="pip-main" x="2" y="9" width="20" height="22"/><ellipse class="pip-shadow" cx="12" cy="44" rx="8" ry="2"/></symbol>
    <symbol id="pip-spade" viewBox="0 0 24 50"><use href="#spade" class="pip-top" x="8" y="0" width="8" height="8"/><use href="#spade" class="pip-main" x="2" y="9" width="20" height="20"/><ellipse class="pip-shadow" cx="12" cy="44" rx="8" ry="2"/></symbol>
    <symbol id="pip-club" viewBox="0 0 24 50"><use href="#club" class="pip-top" x="8" y="0" width="8" height="8"/><use href="#club" class="pip-main" x="2" y="9" width="20" height="20"/><ellipse class="pip-shadow" cx="12" cy="44" rx="8" ry="2"/></symbol>
    <symbol id="ace-heart" viewBox="0 0 46 80"><use href="#heart" class="big" x="3" y="4" width="40" height="40"/><ellipse class="pip-shadow" cx="23" cy="70" rx="18" ry="4"/></symbol>
    <symbol id="ace-diamond" viewBox="0 0 46 80"><use href="#diamond" class="big" x="5" y="2" width="36" height="44"/><ellipse class="pip-shadow" cx="23" cy="70" rx="18" ry="4"/></symbol>
    <symbol id="ace-spade" viewBox="0 0 46 80"><use href="#spade" class="big" x="3" y="4" width="40" height="40"/><ellipse class="pip-shadow" cx="23" cy="70" rx="18" ry="4"/></symbol>
    <symbol id="ace-club" viewBox="0 0 46 80"><use href="#club" class="big" x="3" y="4" width="40" height="40"/><ellipse class="pip-shadow" cx="23" cy="70" rx="18" ry="4"/></symbol>
  </defs>
</svg>

<main class="deck">
  <!-- Hearts -->
  <article class="card"><span class="rank">2</span><svg class="pip"><use href="#pip-heart"/></svg><div class="pattern-band" role="img" aria-label="Decorative triangle pattern"></div></article>
  <article class="card"><span class="rank">3</span><svg class="pip"><use href="#pip-heart"/></svg><div class="pattern-band" role="img" aria-label="Decorative triangle pattern"></div></article>
  <article class="card"><span class="rank">4</span><svg class="pip"><use href="#pip-heart"/></svg><div class="pattern-band" role="img" aria-label="Decorative triangle pattern"></div></article>
  <article class="card"><span class="rank">5</span><svg class="pip"><use href="#pip-heart"/></svg><div class="pattern-band" role="img" aria-label="Decorative triangle pattern"></div></article>
  <article class="card"><span class="rank">6</span><svg class="pip"><use href="#pip-heart"/></svg><div class="pattern-band" role="img" aria-label="Decorative triangle pattern"></div></article>
  <article class="card"><span class="rank">7</span><svg class="pip"><use href="#pip-heart"/></svg><div class="pattern-band" role="img" aria-label="Decorative triangle pattern"></div></article>
  <article class="card"><span class="rank">8</span><svg class="pip"><use href="#pip-heart"/></svg><div class="pattern-band" role="img" aria-label="Decorative triangle pattern"></div></article>
  <article class="card"><span class="rank">9</span><svg class="pip"><use href="#pip-heart"/></svg><div class="pattern-band" role="img" aria-label="Decorative triangle pattern"></div></article>
  <article class="card"><span class="rank">10</span><svg class="pip"><use href="#pip-heart"/></svg><div class="pattern-band" role="img" aria-label="Decorative triangle pattern"></div></article>
  <article class="card"><span class="rank">J</span><div class="face-art" role="img" aria-label="Jack of hearts figure illustration"></div><svg class="corner tr"><use href="#heart"/></svg><svg class="corner bl"><use href="#heart"/></svg><div class="pattern-band" role="img" aria-label="Decorative triangle pattern"></div></article>
  <article class="card"><span class="rank">Q</span><div class="face-art" role="img" aria-label="Queen of hearts figure illustration"></div><svg class="corner tr"><use href="#heart"/></svg><svg class="corner bl"><use href="#heart"/></svg><div class="pattern-band" role="img" aria-label="Decorative triangle pattern"></div></article>
  <article class="card"><span class="rank">K</span><div class="face-art" role="img" aria-label="King of hearts figure illustration"></div><svg class="corner tr"><use href="#heart"/></svg><svg class="corner bl"><use href="#heart"/></svg><div class="pattern-band" role="img" aria-label="Decorative triangle pattern"></div></article>
  <article class="card"><span class="rank">A</span><svg class="ace-pip"><use href="#ace-heart"/></svg></article>

  <!-- Diamonds -->
  <article class="card"><span class="rank">2</span><svg class="pip"><use href="#pip-diamond"/></svg><div class="pattern-band" role="img" aria-label="Decorative triangle pattern"></div></article>
  <article class="card"><span class="rank">3</span><svg class="pip"><use href="#pip-diamond"/></svg><div class="pattern-band" role="img" aria-label="Decorative triangle pattern"></div></article>
  <article class="card"><span class="rank">4</span><svg class="pip"><use href="#pip-diamond"/></svg><div class="pattern-band" role="img" aria-label="Decorative triangle pattern"></div></article>
  <article class="card"><span class="rank">5</span><svg class="pip"><use href="#pip-diamond"/></svg><div class="pattern-band" role="img" aria-label="Decorative triangle pattern"></div></article>
  <article class="card"><span class="rank">6</span><svg class="pip"><use href="#pip-diamond"/></svg><div class="pattern-band" role="img" aria-label="Decorative triangle pattern"></div></article>
  <article class="card"><span class="rank">7</span><svg class="pip"><use href="#pip-diamond"/></svg><div class="pattern-band" role="img" aria-label="Decorative triangle pattern"></div></article>
  <article class="card"><span class="rank">8</span><svg class="pip"><use href="#pip-diamond"/></svg><div class="pattern-band" role="img" aria-label="Decorative triangle pattern"></div></article>
  <article class="card"><span class="rank">9</span><svg class="pip"><use href="#pip-diamond"/></svg><div class="pattern-band" role="img" aria-label="Decorative triangle pattern"></div></article>
  <article class="card"><span class="rank">10</span><svg class="pip"><use href="#pip-diamond"/></svg><div class="pattern-band" role="img" aria-label="Decorative triangle pattern"></div></article>
  <article class="card"><span class="rank">J</span><div class="face-art" role="img" aria-label="Jack of diamonds figure illustration"></div><svg class="corner tr"><use href="#diamond"/></svg><svg class="corner bl"><use href="#diamond"/></svg><div class="pattern-band" role="img" aria-label="Decorative triangle pattern"></div></article>
  <article class="card"><span class="rank">Q</span><div class="face-art" role="img" aria-label="Queen of diamonds figure illustration"></div><svg class="corner tr"><use href="#diamond"/></svg><svg class="corner bl"><use href="#diamond"/></svg><div class="pattern-band" role="img" aria-label="Decorative triangle pattern"></div></article>
  <article class="card"><span class="rank">K</span><div class="face-art" role="img" aria-label="King of diamonds figure illustration"></div><svg class="corner tr"><use href="#diamond"/></svg><svg class="corner bl"><use href="#diamond"/></svg><div class="pattern-band" role="img" aria-label="Decorative triangle pattern"></div></article>
  <article class="card"><span class="rank">A</span><svg class="ace-pip"><use href="#ace-diamond"/></svg></article>

  <!-- Spades -->
  <article class="card"><span class="rank">2</span><svg class="pip"><use href="#pip-spade"/></svg><div class="pattern-band" role="img" aria-label="Decorative triangle pattern"></div></article>
  <article class="card"><span class="rank">3</span><svg class="pip"><use href="#pip-spade"/></svg><div class="pattern-band" role="img" aria-label="Decorative triangle pattern"></div></article>
  <article class="card"><span class="rank">4</span><svg class="pip"><use href="#pip-spade"/></svg><div class="pattern-band" role="img" aria-label="Decorative triangle pattern"></div></article>
  <article class="card"><span class="rank">5</span><svg class="pip"><use href="#pip-spade"/></svg><div class="pattern-band" role="img" aria-label="Decorative triangle pattern"></div></article>
  <article class="card"><span class="rank">6</span><svg class="pip"><use href="#pip-spade"/></svg><div class="pattern-band" role="img" aria-label="Decorative triangle pattern"></div></article>
  <article class="card"><span class="rank">7</span><svg class="pip"><use href="#pip-spade"/></svg><div class="pattern-band" role="img" aria-label="Decorative triangle pattern"></div></article>
  <article class="card"><span class="rank">8</span><svg class="pip"><use href="#pip-spade"/></svg><div class="pattern-band" role="img" aria-label="Decorative triangle pattern"></div></article>
  <article class="card"><span class="rank">9</span><svg class="pip"><use href="#pip-spade"/></svg><div class="pattern-band" role="img" aria-label="Decorative triangle pattern"></div></article>
  <article class="card"><span class="rank">10</span><svg class="pip"><use href="#pip-spade"/></svg><div class="pattern-band" role="img" aria-label="Decorative triangle pattern"></div></article>
  <article class="card"><span class="rank">J</span><div class="face-art" role="img" aria-label="Jack of spades figure illustration"></div><svg class="corner tr"><use href="#spade"/></svg><svg class="corner bl"><use href="#spade"/></svg><div class="pattern-band" role="img" aria-label="Decorative triangle pattern"></div></article>
  <article class="card"><span class="rank">Q</span><div class="face-art" role="img" aria-label="Queen of spades figure illustration"></div><svg class="corner tr"><use href="#spade"/></svg><svg class="corner bl"><use href="#spade"/></svg><div class="pattern-band" role="img" aria-label="Decorative triangle pattern"></div></article>
  <article class="card"><span class="rank">K</span><div class="face-art" role="img" aria-label="King of spades figure illustration"></div><svg class="corner tr"><use href="#spade"/></svg><svg class="corner bl"><use href="#spade"/></svg><div class="pattern-band" role="img" aria-label="Decorative triangle pattern"></div></article>
  <article class="card"><span class="rank">A</span><svg class="ace-pip"><use href="#ace-spade"/></svg></article>

  <!-- Clubs -->
  <article class="card"><span class="rank">2</span><svg class="pip"><use href="#pip-club"/></svg><div class="pattern-band" role="img" aria-label="Decorative triangle pattern"></div></article>
  <article class="card"><span class="rank">3</span><svg class="pip"><use href="#pip-club"/></svg><div class="pattern-band" role="img" aria-label="Decorative triangle pattern"></div></article>
  <article class="card"><span class="rank">4</span><svg class="pip"><use href="#pip-club"/></svg><div class="pattern-band" role="img" aria-label="Decorative triangle pattern"></div></article>
  <article class="card"><span class="rank">5</span><svg class="pip"><use href="#pip-club"/></svg><div class="pattern-band" role="img" aria-label="Decorative triangle pattern"></div></article>
  <article class="card"><span class="rank">6</span><svg class="pip"><use href="#pip-club"/></svg><div class="pattern-band" role="img" aria-label="Decorative triangle pattern"></div></article>
  <article class="card"><span class="rank">7</span><svg class="pip"><use href="#pip-club"/></svg><div class="pattern-band" role="img" aria-label="Decorative triangle pattern"></div></article>
  <article class="card"><span class="rank">8</span><svg class="pip"><use href="#pip-club"/></svg><div class="pattern-band" role="img" aria-label="Decorative triangle pattern"></div></article>
  <article class="card"><span class="rank">9</span><svg class="pip"><use href="#pip-club"/></svg><div class="pattern-band" role="img" aria-label="Decorative triangle pattern"></div></article>
  <article class="card"><span class="rank">10</span><svg class="pip"><use href="#pip-club"/></svg><div class="pattern-band" role="img" aria-label="Decorative triangle pattern"></div></article>
  <article class="card"><span class="rank">J</span><div class="face-art" role="img" aria-label="Jack of clubs figure illustration"></div><svg class="corner tr"><use href="#club"/></svg><svg class="corner bl"><use href="#club"/></svg><div class="pattern-band" role="img" aria-label="Decorative triangle pattern"></div></article>
  <article class="card"><span class="rank">Q</span><div class="face-art" role="img" aria-label="Queen of clubs figure illustration"></div><svg class="corner tr"><use href="#club"/></svg><svg class="corner bl"><use href="#club"/></svg><div class="pattern-band" role="img" aria-label="Decorative triangle pattern"></div></article>
  <article class="card"><span class="rank">K</span><div class="face-art" role="img" aria-label="King of clubs figure illustration"></div><svg class="corner tr"><use href="#club"/></svg><svg class="corner bl"><use href="#club"/></svg><div class="pattern-band" role="img" aria-label="Decorative triangle pattern"></div></article>
  <article class="card"><span class="rank">A</span><svg class="ace-pip"><use href="#ace-club"/></svg></article>

  <!-- Joker and card back -->
  <article class="card joker"><span class="joker-mark">J</span><span class="joker-label">Joker</span><div class="pattern-band" role="img" aria-label="Decorative triangle pattern"></div></article>
  <article class="card card-back">
    <div class="pattern-band top" role="img" aria-label="Decorative triangle pattern"></div>
    <span class="back-title">Card Name</span>
    <svg class="ribbon" viewBox="0 0 64 20" aria-hidden="true"><path d="M0 4Q32 -2 64 4L60 11L64 18Q32 12 0 18L4 11Z"/></svg>
    <div class="pattern-band" role="img" aria-label="Decorative triangle pattern"></div>
  </article>
</main>
</body>
</html>
```